Cercle doré
Zielgruppe
Branche: klassische Musik; Musikgruppe: Klaviertrio (Geige, Cello, Klavier) Gesucht wird ein Flyer, den wir zur Aussendarstellung nutzen können. Zielgruppe sind Veranstalter von klassisch-konservativen Konzerten. Inhalt: Fotos der 3 MusikerInnen, 3x Porträtfoto, 1 Gesamtfoto, 3 Biografien, 1 Text zu unserem Klaviertrio. Der Flyer soll hauptsächlich per mail versandt werden, eine geringe Stückzahl soll ausgedruckt werden.
Format: DIN lang105 QUER !! 210 x 105 mm Vorder- und Rückseite ODER:
DIN lang 105 quer Einbruchfalz
Aufgabenstellung
Das Klaviertrio heisst "Cercle doré", wir spielen hauptsächlich klassisch-romantische Werke. Das Design sollte klassisch-romantisch, aber nicht zu verschnörkelt sein.

```html
<!DOCTYPE html>
<html lang="de">
<head>
<meta charset="utf-8">
<title>Cercle doré – Klaviertrio</title>
<link href="https://fonts.googleapis.com/css2?family=Esteban&family=Yanone+Kaffeesatz:wght@400;500&display=swap" rel="stylesheet">
<style>
  :root {
    --paper: #ffffff;
    --wine: #3d0809;
    --cream: #fbf3ea;
    --photo-light: #e9e6e4;
    --photo-rose: #b98a7a;
    --photo-dark: #3a3434;
    --photo-warm: #c9a47a;
  }
  * { margin: 0; padding: 0; box-sizing: border-box; }
  html, body { width: 1200px; height: 600px; overflow: hidden; background: var(--paper); }
  .flyer {
    position: relative; width: 1200px; height: 600px; background: var(--paper);
  }
  .panel {
    position: absolute; left: 15px; top: 13px; width: 1171px; height: 573px;
    background: var(--wine); color: var(--cream);
  }
  .photo { position: absolute; }
  .photo--violin { left: 27px; top: 22px; width: 137px; height: 206px;
    background: linear-gradient(160deg, var(--photo-light) 30%, var(--photo-rose) 70%, #7a2a2c); }
  .photo--piano { left: 639px; top: 22px; width: 143px; height: 214px;
    background: linear-gradient(165deg, var(--photo-light) 20%, #6b6a70 55%, var(--photo-dark)); }
  .photo--cello { left: 26px; top: 299px; width: 142px; height: 213px;
    background: linear-gradient(150deg, var(--photo-light) 15%, #5b6a5e 50%, var(--photo-warm) 80%); }
  .photo--group { left: 640px; top: 304px; width: 141px; height: 211px;
    background: linear-gradient(180deg, #f1efed 30%, #5a4a44 55%, var(--photo-warm)); }
  .caption {
    position: absolute; font-family: "Yanone Kaffeesatz", sans-serif; font-size: 17px;
    line-height: 18px; text-align: center; width: 180px;
  }
  .caption--violin { left: 5px; top: 236px; }
  .caption--piano { left: 620px; top: 240px; }
  .caption--cello { left: 7px; top: 522px; }
  .bio {
    position: absolute; font-family: "Esteban", serif; font-size: 14.6px;
    line-height: 22.2px; text-align: center; white-space: nowrap;
  }
  .bio--violin { left: 196px; width: 400px; top: 24px; }
  .bio--piano { left: 808px; width: 350px; top: 22px; }
  .bio--cello { left: 196px; width 400px; width: 400px; top: 297px; }
  .contact {
    position: absolute; left: 820px; width: 330px; top: 343px; text-align: center;
    font-family: "Yanone Kaffeesatz", sans-serif; font-weight: 500; font-size: 27px; line-height: 48.5px;
  }
</style>
</head>
<body>
<div class="flyer">
  <section class="panel">
    <div class="photo photo--violin" role="img" aria-label="Porträtfoto der Geigerin mit Violine"></div>
    <p class="caption caption--violin">Réka Somlai, Violine</p>
    <p class="bio bio--violin">Die ungarische Geigerin Réka Somlai hat sich als äu-<br>ßerst vielseitige Musikerin einen Namen gemacht: sie<br>arbeitet als Solistin, Konzertmeisterin und Kammermu-<br>sikerin und gründete darüber hinaus verschiedene er-<br>folgreiche Ensembles. Ihr solistisches Repertoire reicht<br>von den klassischen Violinkonzerten und virtuosen<br>Meisterstücken bis hin zu modernen Kompositionen.<br>Ihre Experimentierfreude ist über Deutschlands Gren-<br>zen hinaus bekannt; zeitgenössische europäische Kom-<br>ponisten arbeiten gerne mit ihr zusammen um neue<br>Klangfarben und Klangfarben zu entwickeln.</p>

    <div class="photo photo--piano" role="img" aria-label="Porträtfoto des Pianisten am Flügel"></div>
    <p class="caption caption--piano">Gábor Ternai, Klavier</p>
    <p class="bio bio--piano">Der Pianist Gábor Ternai ist ebenfalls Ungar<br>und langjähriger Kammermusikpartner von<br>Réka Somlai. Er studierte in Budapest an der<br>Musikakademie am Donauufer und arbeitete an-<br>schließend als Dozent am Aurora Konserva-<br>torium. Seit 1990 lebt und arbeitet Gábor<br>Ternai als Solist und begehrter Begleiter in<br>Deutschland. 1999 gründete der Pianist die Mu-<br>sikschule Ternai in Mülheim und etablierte sich<br>in den folgenden Jahren nicht nur als Pianist<br>sondern auch als erfolgreicher Klavierpädagoge.</p>

    <div class="photo photo--cello" role="img" aria-label="Porträtfoto der Cellistin mit Violoncello"></div>
    <p class="caption caption--cello">Katrin-Luise Ambach,<br>Cello</p>
    <p class="bio bio--cello">Katrin-Luise Ambach wurde in München geboren und<br>spezialisierte sich bereits während ihres Studiums in<br>Würzburg, Nürnberg und Düsseldorf auf die Kam-<br>mermusik. Ihr intensives Streichquartett-Studium<br>vervollständigte sie beim legendären Aurelia Quartett<br>in Stuttgart. Nach zahlreichen Wettbewerbserfolgen<br>und Auszeichnungen widmete sie sich verstärkt zeit-<br>genössischer Musik und der Uraufführung ihr gewid-<br>meter Werke. Katrin-Luise Ambach arbeitete lange Zeit<br>am Lumen Theater in Essen und gilt seitdem auch<br>als viel gefragte Cellistin und Studiomusikerin für<br>Rock- und Pop-Produktionen.</p>

    <div class="photo photo--group" role="img" aria-label="Gruppenfoto des Trios mit Cello, Flügel und Violine in einem hellen Saal"></div>

    <address class="contact" style="font-style: normal;">
      kontakt: Katrin-Luise Ambach<br>
      mobil: +49 170 5550 184<br>
      mail: ambach.trio@postfach-mail.de
    </address>
  </section>
</div>
</body>
</html>
```